Pale Lanterns Old Lane Walk Poster Design

We need an A4 sized poster to promote our weekly true crime tours. This poster will be posted onto community noticeboards.
Lots of information and images can be viewed at the following links:-
www.palelanterns.com.au
www.palelanterns.com.au/bookings/
https://www.facebook.com/palelanternsoldlane/
https://www.examplereviews.com.au/Attraction_Review-g000000-d00000000-Reviews-Pale_Lanterns-Newcastle_Greater_Newcastle_New_South_Wales.html
There are also a number of images for possible use at the following link - we are open to intepretation:-
http://palelanterns.com.au/tour-photographs/
The font on our website is "SpecialElite" so we would like to continue using that font type.
Target Market(s)
Adults 25-65.
Font styles to use
Other font styles liked:
- Special Elite
Colors
Designer to choose colors to be used in the design.
Look and feel
Each slider illustrates characteristics of the customer's brand and the style your logo design should communicate.

```html
<!DOCTYPE html>
<html lang="en">
<head>
<meta charset="utf-8">
<title>Pale Lanterns Old Lane Walk Poster</title>
<link href="https://fonts.googleapis.com/css2?family=Special+Elite&display=swap" rel="stylesheet">
<style>
  :root {
    --backdrop: #6a0e0f;
    --poster: #050505;
    --ink-red: #9c1c1f;
    --ink-light: #eeeaea;
    --fog: #f6eef0;
    --fog-rose: #c99aa2;
    --shade: #3a1c20;
    --badge: #141414;
  }
  * { margin: 0; padding: 0; box-sizing: border-box; }
  html, body {
    width: 1200px; height: 900px; overflow: hidden;
    background: var(--backdrop);
    font-family: "Special Elite", "Courier New", monospace;
  }
  .poster {
    position: absolute; left: 292px; top: 20px;
    width: 615px; height: 860px;
    background: var(--poster);
    overflow: hidden;
    color: var(--ink-light);
  }
  .brand {
    position: absolute; left: 50%; top: 42px;
    transform: translateX(-50%);
    width: 166px; height: 96px;
    border-radius: 50%;
    background: var(--badge);
    display: flex; flex-direction: column; align-items: center; justify-content: center; gap: 8px;
  }
  .brand-dot {
    width: 34px; height: 34px; border-radius: 50%;
    background: var(--ink-light);
  }
  .brand-name {
    font-size: 16px; color: var(--ink-light); letter-spacing: 0.5px;
  }
  .scene-photo {
    position: absolute; left: 60px; top: 205px;
    width: 495px; height: 455px;
    background:
      radial-gradient(ellipse 42% 34% at 50% 30%, var(--fog) 0%, #e8d7db 35%, var(--fog-rose) 60%, rgba(58,28,32,0.7) 80%, rgba(5,5,5,0) 100%),
      radial-gradient(ellipse 50% 40% at 50% 72%, rgba(150,110,115,0.6) 0%, var(--shade) 55%, rgba(5,5,5,0) 100%);
  }
  .tagline-arc {
    position: absolute; left: 0; top: 160px;
    width: 615px; height: 90px;
  }
  .tagline-arc text {
    font-family: "Special Elite", "Courier New", monospace;
    font-size: 24px; fill: var(--ink-light); letter-spacing: 1px;
  }
  .headline {
    position: absolute; left: 0; width: 100%; top: 235px;
    text-align: center;
    font-size: 84px; line-height: 76px;
    color: var(--ink-red);
  }
  .lead-in {
    position: absolute; left: 0; width: 100%; top: 675px;
    text-align: center; font-size: 20px;
  }
  .offer {
    position: absolute; left: 0; width: 100%; top: 712px;
    text-align: center; font-size: 34px;
  }
  .booking {
    position: absolute; left: 0; width: 100%; top: 776px;
    text-align: center; font-size: 18px;
  }
</style>
</head>
<body>
  <main class="poster">
    <div class="brand">
      <span class="brand-dot"></span>
      <span class="brand-name">Pale Lanterns</span>
    </div>

    <div class="scene-photo" role="img" aria-label="Foggy tunnel mouth with a lone figure walking along a cracked path"></div>

    <svg class="tagline-arc" viewBox="0 0 615 90" aria-label="Take a walk on the">
      <defs>
        <path id="arc" d="M172 88 Q307 -2 442 88"/>
      </defs>
      <text><textPath href="#arc" startOffset="50%" text-anchor="middle">TAKE A WALK ON THE</textPath></text>
    </svg>

    <h1 class="headline">DARK<br>SIDE</h1>

    <p class="lead-in">It’d be a crime to miss out on our</p>
    <p class="offer">Weekly True Crime Tours</p>
    <p class="booking">Book now at palelanterns.com.au</p>
  </main>
</body>
</html>
```